Business Card & Logo Design - Hedge Fund

We need a business card and logo design for a hedge fund. The hedge fund is named Morvane Equity LLC. Morvane Equity was created by finance professors and the strategy is based academic research that looks for patterns in stock prices. The design should look conservative, solid, strong. We favor a classic style - nothing flashy. The logo can relate to the name Morvane Equity, or it could involve a symbol design that connotes "science" . We are open to ideas. We do not want alot of colors - but if any, color - blue is preferred. The font that seems to look best for the name (Morvane Equity) is arial black. We are open to ideas. Most important - we want to see a mock up of an actual business card with the logo concept embedded. The business card should include space for : company name, individual name, position title, cell phone, address. We hope to have this work done by Sept. 8.

Target Market(s)

We will be meeting with and giving the business card to institutions and high net worth individuals.

Industry/Entity Type

Investment Advisory

Contact Information for Business Card

Company name - Morvane Equity LLC
Individual name - Peter Dalby
Title - Portfolio Manager
Cell - (412) 555-0187
Address - 2650 Birchmont Lane, Suite 300, Atlanta GA 30327

Font styles to use
Other font styles liked:
• Arial

Colors
3277b5
0255a3
85acd3
cedeed
fdf9cf
d9d9d9
e6e6e6
f04a50
6b449b

Requirements
Must have
• Must have card details that are sited above.
• We would like a logo related to the name (Morvane Equity) or concept of the fund.
Nice to have
• We want conservative / understated / clean crisp look.
• If any colors - we prefer conservative appearance - blue / gray.
• I have enclosed an example of a card style that looks attractive - please do not exactly copy this card. This is not our company or logo. I feel the layout is attractive - just as an example
Should not have
• Avoid too much color.
• I have selected some preferred colors. Please do not use all of the colors - I have selected a few that might work - but I am not sure. We are open to your ideas so please do not feel the need to use all or any of these.

```html
<!DOCTYPE html>
<html lang="en">
<head>
<meta charset="utf-8">
<title>Morvane Equity LLC – Business Card</title>
<link rel="stylesheet" href="https://fonts.googleapis.com/css2?family=Arimo:wght@400;700&display=swap">
<style>
  :root {
    --brand-blue: #0255a3;
    --ink-gray: #3a3a3a;
    --soft-gray: #5a5a5a;
    --paper: #ffffff;
    --backdrop: #e6e6e6;
    --rule-gray: #6b6b6b;
  }
  * { margin: 0; padding: 0; box-sizing: border-box; }
  html, body {
    width: 1200px; height: 582px; overflow: hidden;
    background: var(--backdrop);
    font-family: "Arimo", Arial, sans-serif;
  }
  .canvas { position: relative; width: 1200px; height: 582px; }

  .card {
    position: absolute; top: 50px;
    width: 460px; height: 263px;
    box-shadow: 0 6px 18px rgba(0,0,0,.18);
    overflow: hidden;
  }

  /* Front card */
  .card-front { left: 90px; background: var(--paper); }
  .card-front .band { position: absolute; inset: 0; }
  .card-front .wordmark {
    position: absolute; right: 26px; top: 46px;
    display: flex; align-items: center; gap: 8px;
    font-weight: 700; font-size: 17px; letter-spacing: .5px;
    color: var(--ink-gray);
  }
  .wordmark .mark-square {
    width: 12px; height: 12px; background: var(--brand-blue);
  }
  .card-front .holder {
    position: absolute; left: 28px; top: 104px;
  }
  .holder .person-name {
    font-weight: 700; font-size: 21px; color: var(--ink-gray);
  }
  .holder .person-title {
    font-size: 11px; color: var(--soft-gray); margin-top: 2px;
  }
  .card-front .contact {
    position: absolute; left: 28px; top: 170px;
    color: var(--paper); font-size: 12px; line-height: 19px;
  }
  .contact .phone { display: flex; align-items: center; gap: 6px; }

  /* Back card */
  .card-back {
    left: 650px; background: var(--brand-blue);
    display: flex; align-items: center; justify-content: center;
  }
  .card-back .wordmark {
    display: flex; align-items: center; gap: 10px;
    color: var(--paper); font-weight: 700; font-size: 22px; letter-spacing: 1.5px;
  }
  .card-back .mark-square { width: 14px; height: 14px; background: var(--paper); }

  /* Logo lockup */
  .logo-lockup {
    position: absolute; left: 0; right: 0; top: 410px;
    display: flex; align-items: center; justify-content: center; gap: 14px;
    color: var(--brand-blue); font-weight: 700; font-size: 38px; letter-spacing: 2px;
  }
  .logo-lockup .mark-square { width: 26px; height: 26px; background: var(--brand-blue); }
</style>
</head>
<body>
<main class="canvas">

  <section class="card card-front" aria-label="Business card front">
    <svg class="band" width="460" height="263" viewBox="0 0 460 263">
      <polygon points="0,158 330,158 372,108 460,108 460,263 0,263" fill="var(--brand-blue)"/>
    </svg>
    <div class="wordmark"><span class="mark-square"></span>MORVANE EQUITY</div>
    <div class="holder">
      <p class="person-name">Peter Dalby</p>
      <p class="person-title">Portfolio Manager</p>
    </div>
    <address class="contact" style="font-style:normal">
      <p>2650 Birchmont Lane</p>
      <p>Suite 300, Atlanta GA 30327</p>
      <p class="phone">
        <svg width="9" height="13" viewBox="0 0 9 13" aria-hidden="true">
          <rect x="0.75" y="0.75" width="7.5" height="11.5" rx="1.2" fill="none" stroke="#fff" stroke-width="1.3"/>
          <line x1="3" y1="10" x2="6" y2="10" stroke="#fff" stroke-width="1"/>
        </svg>
        (412) 555-0187
      </p>
    </address>
  </section>

  <section class="card card-back" aria-label="Business card back">
    <div class="wordmark"><span class="mark-square"></span>MORVANE EQUITY LLC</div>
  </section>

  <div class="logo-lockup"><span class="mark-square"></span>MORVANE EQUITY LLC</div>

</main>
</body>
</html>
```